Business Card Design

We offer Procurement, Supply Chain, Merchandise Expediting, Customs Management, Shipping Documentation and many other Specialized Consultancies. The many products we handle are used in many different industries like Oil, Gas and Drilling Hardware, Construction Equipment, Industrial Parts and much more.
Our Slogan is:
"We look from around the world for what you need, bringing it to your door in the shortest possible time with the best all inclusive price"

Target Market(s)

US Export companies, Mexican Import companies and others companies that are looking for Oil & Gas products

Industry/Entity Type

Business

Contact Information for Business Card

Morvenet Trade Partners & Sourcing, LLC
Phone: +1 (281) 555-0163
41853 Brindlecove Pkwy, Ste 1700
Katy, Texas 77392 USA
www.morvenet.biz

Font styles to use
Other font styles liked:
• Century Gothic

```html
<!DOCTYPE html>
<html lang="en">
<head>
<meta charset="UTF-8">
<title>Morvenet Trade Partners &amp; Sourcing – Business Card</title>
<link href="https://fonts.googleapis.com/css2?family=Mulish:wght@400;800&display=swap" rel="stylesheet">
<style>
  :root {
    --brand-red: #f23a42;
    --brand-green: #0b7a4b;
    --card-white: #ffffff;
    --ink-grey: #4a4a4a;
    --backdrop: #e9e6e2;
  }
  * { box-sizing: border-box; margin: 0; padding: 0; }
  html, body {
    width: 1200px; height: 675px; overflow: hidden;
    background: var(--backdrop);
    font-family: "Mulish", "Century Gothic", sans-serif;
  }
  .stage { position: relative; width: 1200px; height: 675px; }
  .card {
    position: absolute; top: 189px;
    width: 520px; height: 297px;
    border-radius: 3px; overflow: hidden;
    box-shadow: 0 10px 28px rgba(0,0,0,0.18);
  }

  /* Company name, set as plain text in one colour and one weight */
  .company-name {
    font-weight: 800; line-height: 1.1; white-space: nowrap;
  }
  .company-name span { display: block; }

  /* Front */
  .card-front { left: 60px; background: var(--card-white); }
  .card-front .company-name {
    position: absolute; right: 28px; top: 58px;
    color: var(--brand-green); text-align: right;
  }
  .card-front .company-main { font-size: 30px; }
  .card-front .company-rest { font-size: 12px; margin-top: 2px; }

  .contact { position: absolute; left: 36px; top: 96px; color: var(--ink-grey); }
  .contact-name { font-size: 16px; font-weight: 800; color: var(--brand-green); }
  .contact-title { font-size: 10.5px; margin-top: 1px; }
  .contact-address { font-size: 11px; line-height: 1.35; margin-top: 18px; }
  .contact-line { display: flex; align-items: center; gap: 8px; font-size: 11px; margin-top: 5px; }
  .contact-line svg { width: 10px; height: 10px; flex: none; }

  .band { position: absolute; bottom: 0; height: 26px; }
  .band-green { left: 0; width: 43%; background: var(--brand-green); }
  .band-red { left: 43%; right: 0; background: var(--brand-red); }

  /* Back */
  .card-back { left: 620px; background: var(--brand-red); }
  .card-back .company-name {
    position: absolute; left: 70px; top: 92px; color: var(--card-white);
  }
  .card-back .company-main { font-size: 54px; }
  .card-back .company-rest { font-size: 21px; margin-top: 4px; }
  .back-web {
    position: absolute; right: 40px; bottom: 34px;
    font-size: 12px; color: var(--card-white);
  }
</style>
</head>
<body>
<main class="stage">
  <section class="card card-front" aria-label="Business card front">
    <div class="contact">
      <p class="contact-name">Dario Velmont</p>
      <p class="contact-title">President CEO</p>
      <p class="contact-address">41853 Brindlecove Pkwy,<br>Ste 1700 Katy,<br>Texas 77392 USA</p>
      <p class="contact-line">
        <svg viewBox="0 0 10 10" aria-hidden="true"><rect x="0.5" y="4" width="9" height="5.5" rx="1" fill="var(--brand-red)"/><path d="M0.5 4 Q5 0 9.5 4" stroke="var(--brand-red)" stroke-width="1.6" fill="none"/></svg>
        +1 (281) 555-0163
      </p>
      <p class="contact-line">
        <svg viewBox="0 0 10 10" aria-hidden="true"><circle cx="5" cy="5" r="4.5" fill="var(--brand-red)"/><path d="M0.5 5H9.5M5 0.5V9.5" stroke="#fff" stroke-width="0.8"/><ellipse cx="5" cy="5" rx="2" ry="4.5" stroke="#fff" stroke-width="0.8" fill="none"/></svg>
        www.morvenet.biz
      </p>
    </div>
    <p class="company-name">
      <span class="company-main">Morvenet</span>
      <span class="company-rest">Trade Partners &amp; Sourcing, LLC</span>
    </p>
    <div class="band band-green"></div>
    <div class="band band-red"></div>
  </section>

  <section class="card card-back" aria-label="Business card back">
    <p class="company-name">
      <span class="company-main">Morvenet</span>
      <span class="company-rest">Trade Partners &amp; Sourcing, LLC</span>
    </p>
    <p class="back-web">www.morvenet.biz</p>
  </section>
</main>
</body>
</html>
```